Our architectural studio needs a new business card

We need a business card design for our studio based in Waterloo in Belgium. We are active in architecture, design and installation.
Our works are contemporary and minimalist. our clients are refined and cultured.
Our business card must be minimalist and refined.

Project Deadline Extended
Reason: Some designers have accepted my invitation but they don't have all replied. I want to give them a chance to make one proposal. Paul

Target Market(s)

architecture

Industry/Entity Type

Business

Contact Information for Business Card

studio: paul dornevaux studio
paul dornevaux, architecte
M. +32 471 586 927
F. +322 619 4850
www.pauldornevaux-example.com
paul@pauldornevaux-example.com
14 rue des Marronniers
1420 Waterloo
Belgium

Font styles to use
Sans Serif

Requirements
Must have
• simple, minimalist, clear, elegant and chic! Black and white
Nice to have
• embossed logo, other format like a square for example
Should not have
• color, fantasy, curves, ...

```html
<!DOCTYPE html>
<html lang="fr">
<head>
<meta charset="utf-8">
<title>Paul Dornevaux Studio — Business Card</title>
<link rel="stylesheet" href="https://fonts.googleapis.com/css2?family=Lato:wght@400;700&family=Montserrat:wght@600&display=swap">
<style>
  :root {
    --backdrop: #e3e0dd;
    --card: #ffffff;
    --ink: #1f1f1f;
    --ink-soft: #2b2b2b;
    --rule-faint: #ececec;
    --shadow: rgba(0, 0, 0, 0.18);
  }
  * { margin: 0; padding: 0; box-sizing: border-box; }
  html, body {
    width: 1200px; height: 720px; overflow: hidden;
    background: var(--backdrop);
  }
  .canvas {
    position: relative; width: 1200px; height: 720px;
    display: flex; justify-content: center; align-items: center; gap: 60px;
  }
  .card {
    position: relative; width: 520px; height: 296px;
    background: var(--card);
    box-shadow: 0 6px 18px var(--shadow);
    color: var(--ink);
    font-family: "Lato", sans-serif;
  }
  /* front */
  .front-mark {
    position: absolute; left: 50%; top: 66px; transform: translateX(-50%);
    width: 40px; height: 40px; background: var(--ink-soft);
  }
  .studio-name {
    font-family: "Montserrat", sans-serif; font-weight: 600;
    text-transform: uppercase; letter-spacing: 0.26em; font-size: 12px;
    color: var(--ink-soft); white-space: nowrap;
  }
  .front .studio-name {
    position: absolute; left: 0; right: 0; top: 224px; text-align: center;
    padding-left: 0.26em;
  }
  /* back */
  .back-divider-faint {
    position: absolute; left: 140px; top: 0; bottom: 0; width: 2px;
    background: var(--rule-faint);
  }
  .back-mark {
    position: absolute; right: 108px; top: 26px;
    width: 36px; height: 36px; background: var(--ink-soft);
  }
  .back .studio-name {
    position: absolute; right: 24px; top: 144px; font-size: 11px;
  }
  .back-rule {
    position: absolute; left: 0; right: 0; top: 168px; height: 2px;
    background: var(--ink);
  }
  .person {
    position: absolute; left: 25px; top: 180px; font-size: 15px;
  }
  .person strong { font-weight: 700; }
  .phones {
    position: absolute; left: 25px; top: 223px; list-style: none;
    font-size: 13.5px; line-height: 18px;
  }
  .phones li { display: flex; align-items: center; gap: 5px; }
  .phones svg { width: 11px; height: 11px; fill: var(--ink); }
  .contact {
    position: absolute; right: 24px; top: 206px; text-align: right;
    font-size: 13.5px; line-height: 18px; font-style: normal;
  }
  .contact .gap { margin-top: 4px; }
</style>
</head>
<body>
<main class="canvas">
  <section class="card front" aria-label="Recto">
    <div class="front-mark"></div>
    <p class="studio-name">Paul Dornevaux Studio</p>
  </section>

  <section class="card back" aria-label="Verso">
    <div class="back-divider-faint"></div>
    <div class="back-mark"></div>
    <p class="studio-name">Paul Dornevaux Studio</p>
    <div class="back-rule"></div>
    <p class="person"><strong>Paul Dornevaux</strong> / Architecte</p>
    <ul class="phones">
      <li>
        <svg viewBox="0 0 24 24" aria-hidden="true"><path d="M6.6 10.8a15.1 15.1 0 0 0 6.6 6.6l2.2-2.2c.3-.3.7-.4 1-.2 1.1.4 2.3.6 3.6.6.6 0 1 .4 1 1V20c0 .6-.4 1-1 1C10.6 21 3 13.4 3 4c0-.6.4-1 1-1h3.5c.6 0 1 .4 1 1 0 1.3.2 2.5.6 3.6.1.3 0 .7-.2 1z"/></svg>
        +32 471 586 927
      </li>
      <li>
        <svg viewBox="0 0 24 24" aria-hidden="true"><path d="M6 2h12v5H6zM4 8h16a2 2 0 0 1 2 2v7h-4v5H6v-5H2v-7a2 2 0 0 1 2-2zm4 8v4h8v-4z"/></svg>
        +322 619 4850
      </li>
    </ul>
    <address class="contact">
      <div>paul@pauldornevaux-example.com</div>
      <div>www.pauldornevaux-example.com</div>
      <div class="gap">14 rue des Marronniers 1420</div>
      <div>Waterloo Belgium</div>
    </address>
  </section>
</main>
</body>
</html>
```